Norvane Staffing - White Collar Engineering Consultancy

I'm chasing a website to provide high level information about what Norvane Staffing is and service's we provide - only chasing something simple. We are a new white collar secondment/contractor/professional services/consultancy specialising is providing the best consultants into contractor roles.

Our primary industries are energy, gas, pipelines, water processing, power, projects, geographic information systems, design, accounting.

Our people are mechanical,/electrical/civil/process/chemical engineers, project engineers, project managers, technical experts, GIS analysts, integrity engineers, pipeline engineers,

Currently I have this domain registered through Zentrio - https://www.norvanestaffing-example.com/

I'd like to keep this domain but completely overhaul the website to be sleek and follow the logo styling.

Example websites within my industry that I like:
- https://www.brelwickworks-example.com.au/
- https://quarn-example.com.au/
- https://www.hdmtech-example.com.au/

I'd like the winner to code and assist with making the website functional under my domain.

Would like to include:
- industries
- services
- why work with us
- terms and conditions as per attached
- location (Brisbane)
- contact us form, that submits an email to sam.burow@norvanestaffing-example.com
- WorkLinker link

Would definitely be looking to polish the winning result with the designer over the phone or via email.

I will also add some infrastructure photos for use; otherwise please use generic CSG related infrastructure.

Cheers,

Sam

Industry/Entity Type

Energy, resources, gas, mining, geographic information systems, accounting, construction.

Coding

Coded - Design and coding required

Number of Pages Required

4 page

Colors
0054AA
0677BA
7BADD7
CADEEF
E8F1F8

Requirements
Must have
• Refer to project description

```html
<!DOCTYPE html>
<html lang="en">
<head>
<meta charset="utf-8">
<title>Norvane Staffing - White Collar Engineering Consultancy</title>
<link href="https://fonts.googleapis.com/css2?family=Outfit:wght@300;400;500;600;700&display=swap" rel="stylesheet">
<style>
:root{
  --navy:#25286b;
  --navy-deep:#1c1f5c;
  --blue:#0677ba;
  --blue-dark:#0054aa;
  --blue-mid:#7badd7;
  --blue-pale:#cadeef;
  --blue-ice:#e8f1f8;
  --grey-bg:#efeff5;
  --text:#3c3c55;
  --white:#ffffff;
}
*{box-sizing:border-box;margin:0;padding:0}
html,body{width:1200px;height:4955px;overflow:hidden}
body{font-family:"Outfit",sans-serif;color:var(--text);background:var(--white);position:relative}
section,header,footer{position:absolute;left:0;width:1200px;overflow:hidden}
.abs{position:absolute}
.pill{position:absolute;display:flex;align-items:center;justify-content:center;border-radius:20px;font-size:13px;font-weight:500}
.pill-solid{background:var(--blue);color:var(--white)}
.pill-outline{border:1.5px solid var(--blue);color:var(--blue);background:var(--white)}
.section-title{position:absolute;left:0;width:1200px;text-align:center;font-size:34px;font-weight:500;color:var(--navy);letter-spacing:-.5px}
.icon-disc{position:absolute;width:72px;height:72px;border-radius:50%;background:linear-gradient(160deg,#1d8fd3,var(--blue-dark));border:3px solid var(--white);display:flex;align-items:center;justify-content:center}
.icon-disc svg{width:38px;height:38px;stroke:#fff;fill:none;stroke-width:2;stroke-linecap:round;stroke-linejoin:round}

/* header / hero */
.hero{top:0;height:600px;background:linear-gradient(100deg,#202467 0%,#2a2e78 45%,#3b4287 70%,#5a6397 100%)}
.hero-photo{position:absolute;left:520px;top:0;width:680px;height:580px;background:linear-gradient(120deg,rgba(40,44,110,0) 0%,rgba(110,120,160,.55) 55%,rgba(150,160,190,.5) 100%)}
.brand{position:absolute;display:flex;align-items:center;gap:8px;color:var(--white);font-weight:600;font-size:21px}
.brand-dot{width:38px;height:38px;border-radius:50%;background:var(--white)}
.nav{position:absolute;top:26px;left:0;height:32px;width:1200px}
.nav a{position:absolute;top:6px;color:var(--white);text-decoration:none;font-size:13.5px}
.nav .contact-btn{top:0;height:34px;width:120px;border:1.5px solid var(--blue);border-radius:18px;display:flex;align-items:center;justify-content:center}
.social-dot{position:absolute;width:34px;height:34px;border-radius:50%;background:var(--blue)}
.hero h1{position:absolute;left:161px;top:143px;color:var(--white);font-size:44px;line-height:53px;font-weight:300;letter-spacing:-.5px}
.hero h1 strong{font-weight:600}
.hero p{position:absolute;left:161px;top:316px;width:440px;color:var(--white);font-size:14px;line-height:25px}

/* about */
.about{top:600px;height:525px}
.about-ring{position:absolute;left:160px;top:63px;width:346px;height:346px;border-radius:50%;border:4px solid var(--blue);border-right-color:transparent;border-bottom-color:transparent;transform:rotate(-20deg)}
.about-photo{position:absolute;left:172px;top:75px;width:322px;height:322px;border-radius:50%;background:radial-gradient(circle at 40% 40%,#d9e2ec,#8ea3bd 70%,#5f7699)}
.about-badge{position:absolute;left:370px;top:261px;width:186px;height:186px;border-radius:50%;background:var(--navy);border:6px solid var(--white)}
.about h2{position:absolute;left:611px;top:66px;font-size:34px;font-weight:500;color:var(--navy);letter-spacing:-.5px}
.about .quote{position:absolute;left:611px;top:122px;border-left:2px solid var(--blue);padding-left:24px;width:380px;color:var(--blue);font-style:italic;font-size:13.5px;line-height:24px}
.about .body{position:absolute;left:611px;width:420px;font-size:13.5px;line-height:24px}

/* services */
.services{top:1125px;height:612px;background:var(--grey-bg)}
.svc-card{position:absolute;top:129px;width:277px;height:348px;background:var(--white);text-align:center}
.svc-card.active{border-bottom:3px solid var(--blue)}
.svc-img{height:164px}
.svc-card .icon-disc{left:102px;top:128px}
.svc-card h3{margin-top:60px;font-size:16px;font-weight:500;color:var(--navy)}
.svc-card p{margin:10px auto 0;width:210px;font-size:13px;line-height:21px}

/* industries */
.industries{top:1737px;height:488px;background:linear-gradient(180deg,#262a70 0%,#2f3479 50%,#262a6e 100%)}
.ind-bg{position:absolute;inset:0;background:linear-gradient(90deg,rgba(90,100,150,.25),rgba(60,70,130,.1) 50%,rgba(90,100,150,.3))}
.ind{position:absolute;width:150px;text-align:center;color:var(--white);font-size:13.5px;line-height:21px}
.ind .icon-disc{position:relative;margin:0 auto 14px;border-width:0}
.industries .section-title{color:var(--white)}

/* why */
.why{top:2225px;height:515px}
.why .lead{position:absolute;left:270px;top:106px;width:660px;text-align:center;font-size:13.5px;line-height:24px}
.why-card{position:absolute;top:213px;width:277px;height:231px;border:1px solid #dcdce6;text-align:center;padding-top:60px}
.why-card .icon-disc{left:101px;top:-20px}
.why-card h3{font-size:16px;font-weight:500;color:var(--navy);line-height:22px}
.why-card p{margin:8px auto 0;width:210px;font-size:13px;line-height:21px}

/* terms */
.terms{top:2740px;height:516px;background:var(--grey-bg)}
.terms h2{position:absolute;left:161px;top:92px;font-size:34px;font-weight:500;color:var(--navy);letter-spacing:-.5px}
.terms p{position:absolute;left:161px;width:420px;font-size:13.5px;line-height:24px}
.terms-doc{position:absolute;left:663px;top:68px;width:375px;height:384px;background:linear-gradient(180deg,#ffffff,#f4f5f9);border-bottom:3px solid var(--blue);box-shadow:0 2px 8px rgba(0,0,0,.08)}

/* join */
.join{top:3256px;height:311px;background:linear-gradient(90deg,#24286c,#2e3378 50%,#24286c)}
.join .section-title{color:var(--white);top:66px}
.join p{position:absolute;left:225px;top:114px;width:750px;text-align:center;color:var(--white);font-size:13.5px;line-height:23px}

/* news */
.news{top:3567px;height:564px}
.news-card{position:absolute;top:127px;width:277px;height:302px;border:1px solid #dcdce6}
.news-img{height:166px}
.news-date{position:absolute;right:10px;top:0;width:54px;height:56px;background:var(--white);text-align:center;color:var(--navy)}
.news-date b{display:block;font-size:22px;font-weight:600;line-height:30px;margin-top:3px}
.news-date span{font-size:10px}
.news-card h3{margin:24px 0 0 26px;font-size:14px;font-weight:500;color:var(--navy);text-decoration:underline}
.news-card p{margin:4px 0 0 26px;width:220px;font-size:13px;line-height:22px}
.news-card a{display:block;margin:4px 0 0 26px;font-size:13px;color:var(--blue)}

/* contact */
.contact{top:4131px;height:488px}
.map{position:absolute;left:0;top:0;width:600px;height:488px;background:linear-gradient(135deg,#eef0f4,#dde2ea)}
.map-pin{position:absolute;left:298px;top:172px;width:54px;height:54px;border-radius:50%;background:var(--navy);border:4px solid var(--white)}
.contact-panel{position:absolute;left:600px;top:0;width:600px;height:488px;background:#0a6fc0;color:var(--white)}
.contact-panel h2{position:absolute;left:60px;top:58px;font-size:34px;font-weight:500}
.contact-panel .sub{position:absolute;left:60px;top:100px;font-size:13.5px}
.field{position:absolute;border:1.5px solid rgba(255,255,255,.7);border-radius:20px;color:var(--white);font-size:13px;padding-left:26px;display:flex;align-items:center}
.field.area{align-items:flex-start;padding-top:16px;border-radius:18px}
.send{position:absolute;left:60px;top:392px;width:157px;height:35px;border-radius:18px;background:var(--white);color:var(--blue);font-size:13px;font-weight:500;display:flex;align-items:center;justify-content:center}

/* footer */
footer{top:4619px;height:336px;background:linear-gradient(90deg,#1f2364,#2a2e72 60%,#232768)}
footer .brand{left:161px;top:50px}
footer .about-text{position:absolute;left:161px;top:107px;width:320px;color:var(--white);font-size:13px;line-height:24px}
footer .social-dot{left:161px;top:167px}
.f-col{position:absolute;top:58px;color:var(--white)}
.f-col h4{font-size:16px;font-weight:500;margin-bottom:12px}
.f-col li{list-style:none;font-size:13px;line-height:30px}
.f-col li.current{text-decoration:underline}
.f-contact{display:flex;gap:10px;font-size:13px;line-height:21px;margin-bottom:12px}
.f-contact svg{width:14px;height:14px;flex:none;margin-top:3px;stroke:var(--blue-mid);fill:none;stroke-width:2}
.f-contact.phone{font-size:16px;font-weight:600}
.copyright{position:absolute;left:0;top:298px;width:1200px;text-align:center;color:var(--white);font-size:12px}
.rule{position:absolute;left:161px;top:278px;width:878px;height:1px;background:rgba(255,255,255,.15)}
</style>
</head>
<body>

<header class="hero">
  <div class="hero-photo" role="img" aria-label="Industrial processing plant with large steel pipes and tanks"></div>
  <svg class="abs" style="left:0;top:0" width="1200" height="600" viewBox="0 0 1200 600" aria-hidden="true">
    <path d="M0 500 C300 530 480 566 600 578 C720 566 900 530 1200 512 L1200 600 L0 600 Z" fill="#0677ba"/>
    <path d="M0 506 C300 540 480 578 600 590 C720 578 900 540 1200 518 L1200 600 L0 600 Z" fill="#ffffff"/>
    <path d="M0 500 C300 530 480 566 600 578 C720 566 900 530 1200 512" fill="none" stroke="#0054aa" stroke-width="2"/>
  </svg>
  <div class="brand" style="left:161px;top:24px"><span class="brand-dot"></span>Norvane Staffing</div>
  <nav class="nav">
    <a style="left:561px">Home</a>
    <a style="left:629px">About</a>
    <a style="left:697px">Industries</a>
    <a style="left:788px">Services</a>
    <a class="contact-btn" style="left:873px">Contact Us</a>
    <span class="social-dot" style="left:1003px;top:0" aria-label="WorkLinker"></span>
  </nav>
  <h1><strong>Professional Services</strong><br>To Oil, Gas, Energy,<br>Mining &amp; More!</h1>
  <p>Lorem ipsum dolor sit amet, consectetur adipiscing elit, sed do eiusmod tempor incididunt ut labore et dolore.</p>
  <a class="pill pill-solid" style="left:161px;top:389px;width:174px;height:35px">Contact Us Today!</a>
</header>

<section class="about">
  <div class="about-ring"></div>
  <div class="about-photo" role="img" aria-label="Close view of large insulated industrial pipework"></div>
  <div class="about-badge"></div>
  <h2>Norvane Staffing</h2>
  <div class="quote">Lorem Ipsum is simply dummy text of the printing and typesetting industry.</div>
  <p class="body" style="top:190px">When an unknown printer took a galley of type and scrambled it to make a type specimen book. It has survived not only five centuries, but also the leap into electronic typesetting, remaining essentially unchanged. It was popularised in the 1960s with the release of Letraset sheets containing Lorem Ipsum passages.</p>
  <p class="body" style="top:326px">And more recently with desktop publishing software like Aldus PageMaker including versions of Lorem Ipsum.</p>
  <a class="pill pill-outline" style="left:611px;top:407px;width:172px;height:34px">More About Norvane</a>
</section>

<section class="services">
  <h2 class="section-title" style="top:58px">Norvane Services</h2>
  <div class="svc-card" style="left:161px">
    <div class="svc-img" role="img" aria-label="Engineer in hard hat working with machinery" style="background:linear-gradient(135deg,#6c7784,#3c4450 60%,#8a6a45)"></div>
    <span class="icon-disc"><svg viewBox="0 0 24 24"><circle cx="12" cy="12" r="3.5"/><path d="M12 2v3M12 19v3M2 12h3M19 12h3M4.9 4.9l2.1 2.1M17 17l2.1 2.1M4.9 19.1 7 17M17 7l2.1-2.1"/></svg></span>
    <h3>Engineering</h3>
    <p>It is a long established fact that a reader will be distracted by the readable content of a page when looking at its layout.</p>
  </div>
  <div class="svc-card active" style="left:461px">
    <div class="svc-img" role="img" aria-label="Interior of a large industrial processing hall" style="background:linear-gradient(180deg,#3c5fa0,#5a6f9a 50%,#6b6f80)"></div>
    <span class="icon-disc"><svg viewBox="0 0 24 24"><path d="M3 21h18M5 21V11l5 3V11l5 3V6h4v15"/></svg></span>
    <h3>Environment</h3>
    <p>It is a long established fact that a reader will be distracted by the readable content of a page when looking at its layout.</p>
  </div>
  <div class="svc-card" style="left:761px">
    <div class="svc-img" role="img" aria-label="Team reviewing plans at a table" style="background:linear-gradient(135deg,#2c3038,#59606b 55%,#9aa0a8)"></div>
    <span class="icon-disc"><svg viewBox="0 0 24 24"><rect x="3" y="4" width="7" height="6" rx="1"/><rect x="14" y="14" width="7" height="6" rx="1"/><path d="M10 7h4a3 3 0 0 1 3 3v4"/></svg></span>
    <h3>Planning</h3>
    <p>It is a long established fact that a reader will be distracted by the readable content of a page when looking at its layout.</p>
  </div>
  <a class="pill pill-outline" style="left:517px;top:508px;width:166px;height:38px;background:transparent">View All Services</a>
</section>

<section class="industries">
  <div class="ind-bg" role="img" aria-label="Faint backdrop of an industrial refinery skyline"></div>
  <h2 class="section-title" style="top:60px">Our Industries</h2>
  <div class="ind" style="left:123px;top:133px"><span class="icon-disc"><svg viewBox="0 0 24 24"><path d="M12 3l8 3v6c0 5-4 8-8 9-4-1-8-4-8-9V6z"/></svg></span>Defence</div>
  <div class="ind" style="left:285px;top:133px"><span class="icon-disc"><svg viewBox="0 0 24 24"><rect x="5" y="8" width="14" height="12" rx="2"/><path d="M9 8V5h6v3M9 14h6"/></svg></span>Hydrogen</div>
  <div class="ind" style="left:444px;top:133px"><span class="icon-disc"><svg viewBox="0 0 24 24"><rect x="4" y="6" width="16" height="9"/><circle cx="8" cy="18" r="2"/><circle cx="16" cy="18" r="2"/></svg></span>Materials Handling<br>&amp; Processing</div>
  <div class="ind" style="left:604px;top:133px"><span class="icon-disc"><svg viewBox="0 0 24 24"><path d="M4 21h16M7 21V9l5-5 5 5v12M10 14h4"/></svg></span>Mining &amp; Minerals</div>
  <div class="ind" style="left:763px;top:133px"><span class="icon-disc"><svg viewBox="0 0 24 24"><path d="M4 21V9h5v12M9 21V5h6v16M15 21v-9h5v9"/></svg></span>Oil &amp; Gas</div>
  <div class="ind" style="left:923px;top:133px"><span class="icon-disc"><svg viewBox="0 0 24 24"><path d="M3 8h10v10M3 12h6v6M13 8h8M13 12h8"/></svg></span>Pipelines</div>
  <div class="ind" style="left:285px;top:300px"><span class="icon-disc"><svg viewBox="0 0 24 24"><path d="M12 3v18M6 7h12M7 11h10M9 21l3-10 3 10"/></svg></span>Power<br>Distribution</div>
  <div class="ind" style="left:444px;top:300px"><span class="icon-disc"><svg viewBox="0 0 24 24"><path d="M3 15c3-2 6 2 9 0s6 2 9 0M3 19c3-2 6 2 9 0s6 2 9 0M8 11l4-7 4 7"/></svg></span>Power<br>Generation</div>
  <div class="ind" style="left:604px;top:300px"><span class="icon-disc"><svg viewBox="0 0 24 24"><path d="M4 18l3-9h12l-3 9zM9 9l-1 9M14 9l-1 9M5 13h13"/></svg></span>Renewable &amp;<br>Microgrid</div>
  <div class="ind" style="left:763px;top:300px"><span class="icon-disc"><svg viewBox="0 0 24 24"><path d="M4 10h10a4 4 0 0 1 4 4v2M4 6h10M17 19a1.5 1.5 0 0 0 3 0c0-1-1.5-2.5-1.5-2.5S17 18 17 19z"/></svg></span>Water &amp;<br>Wastewater</div>
</section>

<section class="why">
  <h2 class="section-title" style="top:58px">Why Work With Us</h2>
  <p class="lead">Lorem Ipsum is simply dummy text of the printing and typesetting industry. Lorem Ipsum has been the industry's standard dummy text ever since the 1500s, when an unknown.</p>
  <div class="why-card" style="left:161px">
    <span class="icon-disc"><svg viewBox="0 0 24 24"><circle cx="12" cy="12" r="8"/><circle cx="12" cy="10" r="2.5"/><path d="M7.5 17c1-2 2.7-3 4.5-3s3.5 1 4.5 3"/></svg></span>
    <h3>Client-centric Approach</h3>
    <p>It is a long established fact that a reader will be distracted by the readable content of a page when looking at its layout. The point of using Lorem Ipsum.</p>
  </div>
  <div class="why-card" style="left:461px">
    <span class="icon-disc"><svg viewBox="0 0 24 24"><circle cx="12" cy="12" r="3"/><path d="M12 3v4M12 17v4M3 12h4M17 12h4M5.6 5.6l2.8 2.8M15.6 15.6l2.8 2.8M5.6 18.4l2.8-2.8M15.6 8.4l2.8-2.8"/></svg></span>
    <h3>Specialist Capabilities</h3>
    <p>It is a long established fact that a reader will be distracted by the readable content of a page when looking at its layout. The point of using Lorem Ipsum.</p>
  </div>
  <div class="why-card" style="left:761px">
    <span class="icon-disc"><svg viewBox="0 0 24 24"><path d="M3 17h4l5 2 8-4-1.5-1.5L13 15H9M3 13h5l4 2"/><circle cx="15" cy="7" r="3"/></svg></span>
    <h3>Borderless, Wide<br>Reaching Support</h3>
    <p>It is a long established fact that a reader will be distracted by the readable content of a page when looking at its layout. The point of using Lorem Ipsum.</p>
  </div>
</section>

<section class="terms">
  <h2>Terms &amp; Conditions</h2>
  <p style="top:146px">It is a long established fact that a reader will be distracted by the readable content of a page when looking at its layout. The point of using Lorem Ipsum is that it has a more-or-less normal distribution of letters, as opposed to using 'Content here, content here', making it look like readable English.</p>
  <p style="top:282px">Many desktop publishing packages and web page editors now use Lorem Ipsum as their default model text, and a search for 'lorem ipsum' will uncover many web sites still in their infancy.</p>
  <a class="pill pill-outline" style="left:161px;top:381px;width:174px;height:34px;background:transparent">
    <svg width="14" height="14" viewBox="0 0 24 24" fill="none" stroke="#0677ba" stroke-width="2" style="margin-right:10px"><path d="M6 3h9l4 4v14H6zM12 10v7M9 14l3 3 3-3"/></svg>Download PDF</a>
  <div class="terms-doc" role="img" aria-label="Preview of the first page of the terms and conditions document"></div>
</section>

<section class="join">
  <div class="abs" style="inset:0;background:linear-gradient(90deg,rgba(100,110,160,.2),rgba(0,0,0,0) 50%,rgba(100,110,160,.2))" role="img" aria-label="Faint backdrop of an industrial site"></div>
  <h2 class="section-title">Join The Team</h2>
  <p>When an unknown printer took a galley of type and scrambled it to make a type specimen book. It has survived not only five centuries, but also the leap into electronic typesetting, remaining essentially unchanged. It was popularised in the 1960s with the release of Letraset sheets containing Lorem Ipsum passages.</p>
  <a class="pill pill-solid" style="left:513px;top:209px;width:172px;height:35px">Contact Us Today!</a>
</section>

<section class="news">
  <h2 class="section-title" style="top:58px">Latest News</h2>
  <div class="news-card" style="left:161px">
    <div class="news-img" role="img" aria-label="Aerial view of a refinery with storage tanks" style="background:linear-gradient(180deg,#8aa6c6,#7a7f86 55%,#5d6570)"></div>
    <div class="news-date"><b>07</b><span>OCT 23</span></div>
    <h3>Lorem Ipsum is simply dummy</h3>
    <p>It is a long established fact that a reader will be distracted by the...</p>
    <a>Read More...</a>
  </div>
  <div class="news-card" style="left:461px">
    <div class="news-img" role="img" aria-label="Pipework and valves inside a processing plant" style="background:linear-gradient(135deg,#3c4148,#7c838c 55%,#b8bdc3)"></div>
    <div class="news-date"><b>05</b><span>OCT 23</span></div>
    <h3>Lorem Ipsum is simply dummy</h3>
    <p>It is a long established fact that a reader will be distracted by the...</p>
    <a>Read More...</a>
  </div>
  <div class="news-card" style="left:761px">
    <div class="news-img" role="img" aria-label="Looking up at tall industrial towers against the sky" style="background:linear-gradient(160deg,#4a6b93,#8aa9cc 50%,#c9d9ea)"></div>
    <div class="news-date"><b>01</b><span>OCT 23</span></div>
    <h3>Lorem Ipsum is simply dummy</h3>
    <p>It is a long established fact that a reader will be distracted by the...</p>
    <a>Read More...</a>
  </div>
  <a class="pill pill-outline" style="left:525px;top:460px;width:150px;height:38px">View All News</a>
</section>

<section class="contact">
  <div class="map" role="img" aria-label="Street map of the Brisbane office location"></div>
  <span class="map-pin"></span>
  <div class="contact-panel">
    <h2>Contact Us</h2>
    <p class="sub">It is a long established fact that a reader will be distracted.</p>
    <div class="field" style="left:60px;top:148px;width:203px;height:37px">Sam |</div>
    <div class="field" style="left:279px;top:148px;width:202px;height:37px">Last Name*</div>
    <div class="field" style="left:60px;top:203px;width:203px;height:37px">Email Address*</div>
    <div class="field" style="left:279px;top:203px;width:202px;height:37px">Phone Number*</div>
    <div class="field area" style="left:60px;top:261px;width:421px;height:110px">Your Message...</div>
    <div class="send">Send Message</div>
  </div>
</section>

<footer>
  <div class="abs" style="inset:0;background:linear-gradient(90deg,rgba(0,0,0,0),rgba(120,130,170,.18))" role="img" aria-label="Faint backdrop of industrial structures"></div>
  <div class="brand"><span class="brand-dot"></span>Norvane Staffing</div>
  <p class="about-text">Lorem ipsum dolor sit amet, consectetur adipiscing elit, sed do eiusmod tempor incididunt.</p>
  <span class="social-dot" aria-label="WorkLinker"></span>
  <div class="f-col" style="left:536px">
    <h4>Quick Links</h4>
    <ul><li class="current">Home</li><li>About</li><li>Industries</li><li>Services</li><li>Contact Us</li></ul>
  </div>
  <div class="f-col" style="left:706px">
    <h4>Our Services</h4>
    <ul><li>Engineering</li><li>Environment</li><li>Planning</li><li>Survey</li></ul>
  </div>
  <div class="f-col" style="left:888px">
    <h4>Our Services</h4>
    <div class="f-contact"><svg viewBox="0 0 24 24"><path d="M12 22s7-7 7-12a7 7 0 0 0-14 0c0 5 7 12 7 12z"/><circle cx="12" cy="10" r="2.5"/></svg><span>48 Kestrel Rd<br>Brisbane, QLD 4000</span></div>
    <div class="f-contact"><svg viewBox="0 0 24 24"><rect x="3" y="5" width="18" height="14" rx="1"/><path d="M3 6l9 7 9-7"/></svg><span>info@norvanestaffing-example.com</span></div>
    <div class="f-contact phone"><svg viewBox="0 0 24 24"><rect x="6" y="2" width="12" height="20" rx="2"/><path d="M11 18h2"/></svg><span>0400 555 018</span></div>
  </div>
  <div class="rule"></div>
  <p class="copyright">© 2023 Norvane Staffing. All Rights Reserved.</p>
</footer>

</body>
</html>
```